依頼概要
■依頼の目的/概要
弊社の経営理念を作成しましたが、社内掲示用にポスターの作成をお願いします。

■依頼詳細
ミッション・ビジョン・バリューをポスター1枚に収めてください。
HPにも掲載できればと考えています。

■重視する点
掲載内容は添付ファイルをご確認ください。

過去の提案(同業者なので)を見て応募しようと考えました。
https://www.pitchora.jp/work/detail/4731852

■弊社の紹介
東京都内で廃棄物を収集・処分する会社です。詳しくは下記Official HPをご覧ください。
https://www.miyakura-k.co.jp

HP検討挿入予定個所
https://www.miyakura-k.co.jp/company

■その他
掲載内容の文言はあまり整理されていないのでうまい具合にご調整ください。

■その他ご不明点はお気軽にお問合せください。

発注時のイメージ通りの作品だったため。

この度は、沢山のご応募ありがとうございます。
皆さんのご提案が多く、選定に迷いました。

また機会がございましたら、よろしくお願いします。

```html
<!DOCTYPE html>
<html lang="ja">
<head>
<meta charset="utf-8">
<title>MIYAKURA 経営理念</title>
<link href="https://fonts.googleapis.com/css2?family=Noto+Sans+JP:wght@400;500;700&family=Roboto:wght@700;900&display=swap" rel="stylesheet">
<style>
  :root {
    --navy: #1c3f8e;
    --violet: #5a2a85;
    --wine: #a3203d;
    --accent-red: #c8323a;
    --text: #2b2b2b;
    --line-start: #1c3f8e;
    --line-end: #8fc3e8;
    --sky-top: #ffffff;
    --sky-mid: #d6e6f2;
    --sky-low: #aac5da;
    --city: #7d8c93;
    --green: #5e7a4a;
    --river: #b9cfdc;
  }
  * { margin: 0; padding: 0; box-sizing: border-box; }
  html, body { width: 879px; height: 1200px; overflow: hidden; background: #fff; }
  body { font-family: "Noto Sans JP", sans-serif; color: var(--text); }

  .poster { position: relative; width: 879px; height: 1200px; overflow: hidden; background: var(--sky-top); }

  .city-photo {
    position: absolute; left: 0; right: 0; top: 560px; bottom: 0;
    background:
      linear-gradient(180deg, rgba(255,255,255,1) 0%, rgba(255,255,255,0) 28%),
      linear-gradient(180deg, var(--sky-top) 0%, var(--sky-mid) 38%, var(--sky-low) 52%, var(--city) 68%, var(--river) 80%, var(--green) 100%);
  }

  .brand { position: absolute; top: 52px; left: 0; right: 0; display: flex; justify-content: center; align-items: center; gap: 14px; }
  .brand-dot { width: 44px; height: 44px; border-radius: 50%; background: var(--navy); }
  .brand-text { display: flex; flex-direction: column; }
  .brand-name { font-family: "Roboto", sans-serif; font-weight: 700; font-size: 36px; letter-spacing: 2px; color: var(--navy); line-height: 1; }
  .brand-sub { font-size: 13px; color: var(--navy); text-align: right; margin-top: 4px; letter-spacing: 1px; }

  .section { position: absolute; left: 52px; right: 52px; }
  .section-head { display: flex; align-items: baseline; gap: 12px; padding-bottom: 6px; position: relative; }
  .section-head::after {
    content: ""; position: absolute; left: 0; right: 0; bottom: 0; height: 3px;
    background: linear-gradient(90deg, var(--line-start), var(--line-end) 70%, rgba(255,255,255,0));
  }
  .section-title { font-family: "Roboto", sans-serif; font-weight: 900; font-size: 50px; line-height: 1; }
  .section-label { font-size: 20px; font-weight: 500; color: var(--accent-red); }
  .mission .section-title { color: var(--navy); }
  .vision .section-title { color: var(--violet); }
  .value .section-title { color: var(--wine); }

  .mission { top: 200px; }
  .mission-body { margin-top: 22px; font-size: 25px; line-height: 1.55; font-weight: 500; }

  .vision { top: 418px; }
  .vision-list { list-style: none; margin-top: 20px; margin-left: 18px; }
  .vision-list li { display: flex; align-items: center; font-size: 25px; line-height: 1.62; font-weight: 500; }
  .vision-key { display: flex; align-items: center; width: 222px; font-family: "Roboto", sans-serif; font-weight: 700; color: var(--violet); }
  .vision-key::before, .value-list li::before {
    content: ""; display: inline-block; width: 17px; height: 17px; border-radius: 50%; margin-right: 9px; flex: none;
  }
  .vision-key::before { background: var(--violet); }

  .value { top: 688px; }
  .value-list { list-style: none; margin-top: 20px; margin-left: 18px; }
  .value-list li { display: flex; align-items: center; font-size: 25px; line-height: 1.62; font-weight: 500; }
  .value-list li::before { background: var(--wine); }

  .copyright { position: absolute; left: 28px; bottom: 22px; font-size: 13px; color: #fff; }
</style>
</head>
<body>
<main class="poster">
  <div class="city-photo" role="img" aria-label="川と緑に囲まれた街並みを見渡す空撮風景"></div>

  <header class="brand">
    <span class="brand-dot"></span>
    <div class="brand-text">
      <span class="brand-name">MIYAKURA</span>
      <span class="brand-sub">株式会社宮倉産業</span>
    </div>
  </header>

  <section class="section mission">
    <div class="section-head">
      <h2 class="section-title">Mission</h2>
      <span class="section-label">社会的使命</span>
    </div>
    <p class="mission-body">地球環境を保全するために、<br>静脈産業を支える社会インフラの一部としての役割を全うし、<br>すべての人に快適でクリーンな世界を提供する。</p>
  </section>

  <section class="section vision">
    <div class="section-head">
      <h2 class="section-title">Vision</h2>
      <span class="section-label">中長期計画</span>
    </div>
    <ul class="vision-list">
      <li><span class="vision-key">Advanced</span>先進的な取り組みを行う。</li>
      <li><span class="vision-key">Lead</span>廃棄物業界をリードする。</li>
      <li><span class="vision-key">High quality</span>高品質なサービスを提供する。</li>
      <li><span class="vision-key">Satisfaction</span>働きがいのある会社づくりを行う。</li>
    </ul>
  </section>

  <section class="section value">
    <div class="section-head">
      <h2 class="section-title">Value</h2>
      <span class="section-label">大切な価値観</span>
    </div>
    <ul class="value-list">
      <li>活発なコミュニケーションによる情報共有。</li>
      <li>チームワーク溢れる組織風土と共働。</li>
      <li>何事にも真摯に向き合う正直な気持ち。</li>
      <li>チャレンジする行動力と自己実現。</li>
    </ul>
  </section>

  <p class="copyright">© MIYAKURA Industry Co., Ltd.</p>
</main>
</body>
</html>
```